We have a small 501C Non-Profit, called Youngsters Unite. The non-profit was started by my son and his friends during the Gulf Oil Spill. We would like to update the website that currently sits on Domivault.com. I'm not sure how we transfer over the domain or get them to host it with your new design. I've attached a link of the old site that we developed. We are open to any ideas regarding hosting.

We would basically like a look that is youth (teen, college age) oriented that will drive teens and donors to the site. Our goal is to get onto Plixa Drives, get grants and make major donations with little to no administration expense. We will get sponsors to pay for the administration costs. So we will be looking for sponsors to support the overhead and 100% of donor money will go to causes important to teens.

http://www.youngstersunite.org

Target Market(s)

Teenagers and Individual Sponsors. Adults that want to help teens with an important cause.

Industry/Entity Type

Non-Profit

Requirements
Must have
• We are very open to ideas. It would be good to have a:

Home-with Mission Statement and Photos or Graphics
Donate-100% of Donations Go To Causes (with Coinvo Link)
Become A Sponsor-Insert Contact Information In This Section.
How It All Got Started -with info, articles, events, video, etc. from Gulf Oil Spill, Our Founder photo.
Contact-Change phone number to 555-804-2739. Keep e-mail and mailing the same.

You can use some existing photos from current site if you would like. All the Recent Event Photos, Founder Photo, 3 people holding check photo were all taken by me so there are no rights issues with those.

YU Mission Statement:

To demonstrate to the world that Youngsters Unite about the environment, each other and world peace through fund raising and other philanthropic efforts.
Nice to have
• Youngsters Unite Logo If Possible

Photo of 3 people, holding check, from existing home page in new History Section.

Kindpaw League Story and Logo in History Section

WRX Video in History Section

Helpio4
http://www.helpio4.net/stories/youth-launches-charity-to-fund-relief-for-wildlife-harmed-by-coastal-slick.html
Should not have
• Delete Blog Section
Delete Founder Section
Delete Recent Events
Delete How To Get Involved

```html
<!DOCTYPE html>
<html lang="en">
<head>
<meta charset="utf-8">
<title>Youngsters Unite</title>
<link href="https://fonts.googleapis.com/css2?family=Arimo:wght@400;700&display=swap" rel="stylesheet">
<style>
:root{
  --bg-deep:#2a4576;
  --bg-mid:#3f629a;
  --bg-light:#5a80b9;
  --ink:#2c2c2c;
  --heading:#2f4f80;
  --white:#ffffff;
  --rule:#dedede;
  --btn-dark:#2d4673;
  --footer:#252525;
  --footer-line:#3a3a3a;
  --link:#3b63b8;
  --green:#6dbb2a;
}
*{box-sizing:border-box;margin:0;padding:0}
html,body{width:841px;height:1200px;overflow:hidden}
body{
  position:relative;
  font-family:"Arimo",Arial,sans-serif;
  background:radial-gradient(ellipse 70% 55% at 50% 60%,var(--bg-light),var(--bg-mid) 55%,var(--bg-deep));
  color:var(--ink);
}
.abs{position:absolute}
/* header */
.brand{left:33px;top:8px;width:321px;height:92px;background:var(--white)}
.brand-frame{position:absolute;inset:8px;border:1px solid #e2e2e2;display:flex;align-items:center;padding-left:12px;gap:8px}
.brand-name{font-size:24px;color:#1d1d1d;letter-spacing:.3px}
.brand-dot{width:38px;height:38px;border-radius:50%;background:#2b4f8f}
.nav-active{left:354px;top:8px;width:51px;height:92px;background:linear-gradient(#2b4372,#4b6da5 50%,#2b4372)}
.nav a{position:absolute;top:50px;font-size:10px;font-weight:700;color:var(--white);text-decoration:none;letter-spacing:.2px}
/* hero */
.hero{left:33px;top:115px;width:775px;height:313px;background:linear-gradient(160deg,#c9c1a8,#8f9a8c 45%,#d9d6cf 70%,#6d7c64)}
/* panel */
.panel{left:33px;top:442px;width:775px;height:245px;background:var(--white)}
.panel-frame{position:absolute;inset:8px;border:1px solid #e4e4e4}
h2{position:absolute;font-size:15px;font-weight:700}
.panel h2{color:var(--heading)}
.lead{position:absolute;font-size:11.5px;font-weight:700;line-height:15.7px;width:205px;color:#333}
.copy{position:absolute;font-size:11.5px;line-height:15.7px;width:205px}
.btn{position:absolute;width:99px;height:19px;font-size:11.5px;font-weight:700;text-align:center;line-height:19px}
.btn-dark{background:linear-gradient(90deg,#22375e,#3e5f93);color:var(--white)}
.btn-light{background:var(--white);color:var(--btn-dark)}
.list{position:absolute;width:98px;list-style:none}
.list li{height:27px;line-height:27px;font-size:10.5px;border-bottom:1px solid var(--rule);padding-left:27px;position:relative;color:#333}
.list li:last-child{border-bottom:none}
.list li::before{content:"";position:absolute;left:15px;top:10px;width:6px;height:6px;border-radius:50%;background:#3d5f92}
/* features */
.features h2{color:var(--white)}
.photo{position:absolute;width:206px;height:118px;background:var(--white)}
.photo span{position:absolute;inset:8px}
.features .copy{color:var(--white);width:220px}
/* footer */
.footer{left:33px;top:1003px;width:775px;height:180px;background:var(--footer)}
.footer-frame{position:absolute;inset:8px;border:1px solid var(--footer-line)}
.signup-title{left:86px;top:1028px;font-size:11.5px;font-weight:700;color:var(--white);line-height:16px}
.field{position:absolute;left:86px;width:132px;height:19px;background:var(--white);font-size:9.5px;color:#888;padding-left:6px;line-height:19px}
.signup-btn{left:86px;top:1132px;width:56px;height:22px;background:linear-gradient(#8bd33c,var(--green));border:1px solid #4a8a1a;color:var(--white);font-size:10.5px;font-weight:700;text-align:center;line-height:20px}
.foot-col{position:absolute;top:1027px}
.foot-col h3{font-size:11.5px;color:var(--white);font-weight:700;margin-bottom:9px}
.foot-col a{display:block;font-size:9.5px;color:var(--link);text-decoration:none;height:19px;font-weight:700}
</style>
</head>
<body>
<header>
  <div class="abs brand"><div class="brand-frame"><span class="brand-name">Youngsters Unite</span><span class="brand-dot"></span></div></div>
  <div class="abs nav-active"></div>
  <nav class="nav">
    <a style="left:364px">HOME</a>
    <a style="left:416px">DONATE</a>
    <a style="left:481px">BECOME A SPONSOR</a>
    <a style="left:608px">HOW IT ALL GOT STARTED</a>
    <a style="left:759px">CONTACT</a>
  </nav>
</header>

<div class="abs hero" role="img" aria-label="Group photo of smiling teen volunteers in matching white charity T-shirts under a wildlife fundraiser banner"></div>

<section class="abs panel">
  <div class="panel-frame"></div>
</section>
<section class="intro">
  <h2 style="left:54px;top:464px">Case Nostrud Suscipit</h2>
  <p class="lead" style="left:54px;top:498px">Quem commodo qui ne, nobis disputando appellantur te pri. Ad</p>
  <p class="copy" style="left:54px;top:544px">Quem commodo qui ne, nobis disputando appellantur te pri. Ad antiopam euripidis vis. Homero animal vocibus eam ut, eu liber vocent appareat sit. Ne mel idque utroque,</p>
  <div class="btn btn-dark" style="left:54px;top:643px">Read more</div>

  <h2 style="left:316px;top:464px">Ea per latine partiendo rebus</h2>
  <ul class="list" style="left:315px;top:490px"><li>Reformidans</li><li>Iuvaret</li><li>Consequuntur</li><li>Ullamcorper</li><li>Essent</li><li>Gloriatur</li></ul>
  <ul class="list" style="left:420px;top:490px"><li>Reformidans</li><li>Iuvaret</li><li>Consequuntur</li><li>Ullamcorper</li><li>Essent</li><li>Gloriatur</li></ul>

  <h2 style="left:582px;top:464px">Case Nostrud Suscipit</h2>
  <p class="lead" style="left:582px;top:498px">Quem commodo qui ne, nobis disputando appellantur te pri. Ad</p>
  <p class="copy" style="left:582px;top:544px">Quem commodo qui ne, nobis disputando appellantur te pri. Ad antiopam euripidis vis. Homero animal vocibus eam ut, eu liber vocent appareat sit. Ne mel idque utroque,</p>
  <div class="btn btn-dark" style="left:582px;top:643px">Read more</div>
</section>

<section class="features">
  <h2 style="left:54px;top:707px">Case Nostrud Suscipit</h2>
  <div class="photo" style="left:54px;top:745px"><span role="img" aria-label="Volunteers handing out items at an outdoor event tent" style="background:linear-gradient(135deg,#c8b89a,#7d6a55 60%,#b0a08a)"></span></div>
  <p class="copy" style="left:54px;top:883px">Quem commodo qui ne, nobis disputando appellantur te pri. Ad antiopam euripidis vis. Homero</p>
  <div class="btn btn-light" style="left:54px;top:950px">Read more</div>

  <h2 style="left:318px;top:707px">Case Nostrud Suscipit</h2>
  <div class="photo" style="left:318px;top:745px"><span role="img" aria-label="Founder standing in a green coastal marsh" style="background:linear-gradient(#c9d3c0,#6f8a4c 55%,#3f5a2a)"></span></div>
  <p class="copy" style="left:318px;top:883px">Quem commodo qui ne, nobis disputando appellantur te pri. Ad antiopam euripidis vis. Homero</p>
  <div class="btn btn-light" style="left:318px;top:950px">Read more</div>

  <h2 style="left:582px;top:707px">Case Nostrud Suscipit</h2>
  <div class="photo" style="left:582px;top:745px"><span role="img" aria-label="Three people presenting a large donation check" style="background:linear-gradient(135deg,#b08a63,#8c6a4c 50%,#d2c7b8)"></span></div>
  <p class="copy" style="left:582px;top:883px">Quem commodo qui ne, nobis disputando appellantur te pri. Ad antiopam euripidis vis. Homero</p>
  <div class="btn btn-light" style="left:582px;top:950px">Read more</div>
</section>

<footer>
  <div class="abs footer"><div class="footer-frame"></div></div>
  <p class="abs signup-title">Sign up for news<br>and updates</p>
  <div class="field" style="top:1070px">Your Name</div>
  <div class="field" style="top:1098px">Email Address</div>
  <div class="abs signup-btn">Sign Up</div>
  <div class="foot-col" style="left:272px"><h3>Subtitle</h3><a>Footer Link</a><a>Footer Link</a><a>Footer Link</a><a>Footer Link</a><a>Footer Link</a><a>Footer Link</a></div>
  <div class="foot-col" style="left:379px"><h3>Subtitle</h3><a>Footer Link</a><a>Footer Link</a><a>Footer Link</a><a>Footer Link</a><a>Footer Link</a><a>Footer Link</a></div>
  <div class="foot-col" style="left:486px"><h3>Subtitle</h3><a>Footer Link</a><a>Footer Link</a><a>Footer Link</a><a>Footer Link</a><a>Footer Link</a><a>Footer Link</a></div>
  <div class="foot-col" style="left:594px"><h3>Subtitle</h3><a>Footer Link</a><a>Footer Link</a><a>Footer Link</a><a>Footer Link</a><a>Footer Link</a><a>Footer Link</a></div>
  <div class="foot-col" style="left:701px"><h3>Subtitle</h3><a>Footer Link</a><a>Footer Link</a><a>Footer Link</a><a>Footer Link</a><a>Footer Link</a><a>Footer Link</a></div>
</footer>
</body>
</html>
```